Website for HVAC products

We would like a website created that is simple and crisp while still mobile friendly. We currently have less than 30 products and we like the layout of the following site:
( http://www.brimlowquintaforge.com/ ).

The color scheme has to blend well with our attached logo.

The menu bar needs to consist of:
Home -
Products- A page with all products
Sub-Pages- Air Handler Stands
Aluminum Condenser Stands
Air Distribution Products
A/C Cages
Accessories
Resources- A page with all specification sheets, instructions,
forms, video's, etc that will be elsewhere but can be
found in one place
Log In- A password protected area that will have special pricing
FAQ- Frequently asked questions / Sales Terms
Contact Us- Map, pics, contact form

The actual product sales page can be similar to the example website above with the following exceptions-
- Main product image with different images available
- Description
- Availability (Not Needed)
- Options (I need to be able to modify)
- Qty
- Add to Cart
- Current "Request a Quote" to be replaced with "Log In for
Distributor Pricing" and redirect to that page
- Description
- Related Products (Not Needed)
- Specifications
- Specifications Metric (Not Needed)

I have no preference on format (I currently use Wordpress) as long as it is user friendly to update/change content, products, images, etc.

In Summary-
The example website is a style we like but it's just an example
Please use our logo and colors
Please use general pictures for the slider until we have some
Please use the lorem ipsum text where info is needed and not
available

Thank you for your interest and I look forward to the creativity

HVAC Distributors

Hvac

• Layout similar to example website
• Mobile Device Capable

```html
<!DOCTYPE html>
<html lang="en">
<head>
<meta charset="utf-8">
<title>Ventora Climate Supply Works</title>
<link rel="stylesheet" href="https://fonts.googleapis.com/css2?family=Ubuntu:wght@400;500;700&family=Arimo:wght@400;700&display=swap">
<style>
:root{
  --blue:#1a7bcb;
  --blue-dark:#0f63ad;
  --red:#b30a0a;
  --red-dark:#8c0404;
  --ink:#333;
  --muted:#555;
  --black:#0e0c0b;
  --white:#fff;
  --steel-light:#e4e6e8;
  --steel:#a9adb1;
  --steel-dark:#5f6367;
}
*{margin:0;padding:0;box-sizing:border-box}
html,body{width:1200px;height:999px;overflow:hidden;background:var(--white);font-family:Arimo,Arial,sans-serif;color:var(--ink)}
.wrap{width:980px;margin:0 auto;position:relative;height:100%}
.topbar{height:51px;background:var(--blue);color:var(--white);font-size:12.5px}
.topbar .wrap{display:flex;justify-content:space-between;align-items:center}
.topbar .phone,.topbar .links{display:flex;align-items:center;gap:6px}
.topbar svg{width:11px;height:11px;fill:var(--white)}
.header{height:83px}
.header .wrap{display:flex;justify-content:space-between;align-items:center}
.brand{display:flex;align-items:center;gap:8px;font-family:Ubuntu,sans-serif;font-weight:700;font-size:30px;color:var(--red);letter-spacing:1px}
.brand .mark{width:24px;height:24px;border-radius:50%;background:var(--blue)}
.search{width:197px;height:45px;border:1px solid #ccc;border-radius:3px;display:flex;align-items:center;justify-content:space-between;padding:0 14px 0 16px;color:#aaa;font-size:12.5px}
.search svg{width:13px;height:13px}
.nav{height:57px;background:linear-gradient(#2288d6,#0d5fa9)}
.nav ul{list-style:none;display:flex;align-items:center;height:57px;font-family:Ubuntu,sans-serif;font-size:12px;color:var(--white)}
.nav li{padding:0 18px;height:37px;line-height:37px;border-radius:3px}
.nav li.active{background:var(--red);margin-left:23px}
.nav li:nth-child(2){margin-left:58px}
.nav li:nth-child(3){margin-left:54px}
.nav li:nth-child(4){margin-left:58px}
.nav li:nth-child(5){margin-left:58px}
.nav li:nth-child(6){margin-left:56px}
.nav li:nth-child(7){margin-left:55px}
.hero{margin-top:28px;height:377px;border:1px solid #ddd;box-shadow:0 0 4px rgba(0,0,0,.2);padding:3px;background:var(--white)}
.slide{position:relative;height:100%;background:linear-gradient(#c9c9c9,#f1f1f1)}
.slide h1{position:absolute;left:63px;top:94px;font-family:Ubuntu,sans-serif;font-weight:700;font-size:24px;color:#2b2b2b;letter-spacing:-.1px}
.slide p{position:absolute;left:63px;top:139px;width:560px;font-size:12.4px;line-height:31px;text-align:justify;color:var(--ink)}
.btn{position:absolute;left:63px;top:236px;width:179px;height:49px;border-radius:3px;background:linear-gradient(var(--red),var(--red-dark));color:var(--white);font-family:Ubuntu,sans-serif;font-weight:500;font-size:15.5px;display:flex;align-items:center;justify-content:center;gap:8px}
.btn svg{width:14px;height:14px}
.slide .photo{position:absolute;left:709px;top:38px;width:167px;height:296px;border-radius:2px;background:linear-gradient(100deg,var(--steel) 0%,var(--steel-light) 35%,#f4f5f6 50%,var(--steel) 75%,var(--steel-dark) 100%)}
.dots{position:absolute;left:460px;top:350px;display:flex;gap:8px}
.dots i{width:7px;height:7px;border-radius:50%;background:#888;display:block}
.dots i.on{background:var(--blue)}
.products{display:flex;margin-top:42px}
.product{width:177px;margin-right:24px}
.product:nth-child(2){margin-right:25px}
.product:last-child{margin-right:0}
.product .thumb{height:148px;border:1px solid #e4e4e4;box-shadow:inset 0 0 8px rgba(0,0,0,.1);padding:9px 12px;background:#f2f2f2}
.product .thumb div{height:100%}
.t-stand{background:radial-gradient(ellipse 45% 48% at 50% 50%,#8a8e92 0%,#b8bbbe 45%,#fff 100%)}
.t-condenser{background:radial-gradient(ellipse 55% 40% at 50% 50%,#9a9ea2 0%,#c8cacd 50%,#fff 100%)}
.t-duct{background:radial-gradient(ellipse 42% 45% at 50% 48%,#7f8387 0%,#c4c7ca 55%,#fff 100%)}
.t-cage{background:radial-gradient(ellipse 50% 38% at 50% 50%,#4d4d45 0%,#b39a3c 45%,#fff 100%)}
.t-accessory{background:radial-gradient(ellipse 40% 45% at 50% 50%,#6f7377 0%,#bfc2c5 50%,#fff 100%)}
.product h2{font-family:Ubuntu,sans-serif;font-weight:400;font-size:13px;color:var(--muted);margin-top:18px;padding-left:1px}
.contactbar{position:absolute;top:856px;left:0;width:1200px;height:70px;background:var(--black);color:var(--white);font-size:12px}
.contactbar .wrap{display:flex;align-items:center}
.contactbar .item{display:flex;align-items:center;gap:8px;margin-right:32px}
.contactbar svg{width:13px;height:13px;fill:var(--blue)}
.social{margin-left:auto;display:flex;gap:7px}
.social i{width:28px;height:28px;border-radius:50%;display:block;border:2px solid rgba(255,255,255,.35)}
.s1{background:#3b5a9a}.s2{background:#3aa4dd}.s3{background:#1c7fb3}.s4{background:#f27b1c}
.copyright{position:absolute;top:926px;left:0;width:1200px;height:73px;background:var(--blue);color:var(--white);font-size:12.5px;text-align:center;line-height:73px}
</style>
</head>
<body>
<div class="topbar"><div class="wrap">
  <div class="phone"><svg viewBox="0 0 12 12"><path d="M2 1l2 0 1 3-1.3 1a6 6 0 0 0 3.3 3.3L8 7l3 1v2c0 .6-.5 1-1 1A9 9 0 0 1 1 2c0-.5.4-1 1-1z"/></svg> TOLL FREE 866.402.3190</div>
  <div class="links">
    <svg viewBox="0 0 12 12"><path d="M0 1h2l1 6h7l1-4H3"/><circle cx="4" cy="10" r="1"/><circle cx="9" cy="10" r="1"/></svg> CART <span>|</span>
    <svg viewBox="0 0 12 12"><path d="M1 1h10v10H1zM3 6l2 2 4-4-1-1-3 3-1-1z" fill-rule="evenodd"/></svg> CHECKOUT <span>|</span>
    <svg viewBox="0 0 12 12"><circle cx="6" cy="3.5" r="2.5"/><path d="M1 11c0-3 2-4.5 5-4.5s5 1.5 5 4.5z"/></svg> MY ACCOUNT <span>|</span>
    <svg viewBox="0 0 12 12"><path d="M6 0a6 6 0 1 0 0 12A6 6 0 0 0 6 0zm0 3a3 3 0 1 1 0 6 3 3 0 0 1 0-6z" fill-rule="evenodd"/></svg> HELP
  </div>
</div></div>
<header class="header"><div class="wrap">
  <div class="brand"><span class="mark"></span>VENTORA</div>
  <div class="search">Search...<svg viewBox="0 0 14 14" fill="none" stroke="#999" stroke-width="2"><circle cx="6" cy="6" r="4.5"/><path d="M9.5 9.5l3.5 3.5"/></svg></div>
</div></header>
<nav class="nav"><div class="wrap"><ul>
  <li class="active">HOME</li><li>PRODUCTS</li><li>RESOURCES</li><li>VIDEOS</li><li>LOGIN</li><li>FAQ</li><li>CONTACT US</li>
</ul></div></nav>
<main class="wrap" style="height:auto">
  <section class="hero"><div class="slide">
    <h1>INSULATED RETURN STAND AIR HANDLER/FURNACE</h1>
    <p>This Insulated Return Air Stand is used where Positive Duct Returns are required. Typical applications would include Garage or Basement Installations where Return Air is brought back to the unit with Ductwork. The Stand supports the Air Handler/Furnace.</p>
    <div class="btn"><svg viewBox="0 0 14 14"><circle cx="7" cy="7" r="7" fill="#fff"/><path d="M6 3h2v3h3v2H8v3H6V8H3V6h3z" fill="#a00"/></svg>MORE DETAILS</div>
    <div class="photo" role="img" aria-label="Photo of an insulated metal return air stand under an air handler box"></div>
    <div class="dots"><i></i><i></i><i class="on"></i><i></i></div>
  </div></section>
  <section class="products">
    <div class="product"><div class="thumb"><div class="t-stand" role="img" aria-label="Photo of a metal air handler stand"></div></div><h2>Air Handler Stands</h2></div>
    <div class="product"><div class="thumb"><div class="t-condenser" role="img" aria-label="Photo of an aluminum condenser stand"></div></div><h2>Aluminum Condenser Stands</h2></div>
    <div class="product"><div class="thumb"><div class="t-duct" role="img" aria-label="Photo of a metal air distribution box"></div></div><h2>Air Distribution Products</h2></div>
    <div class="product"><div class="thumb"><div class="t-cage" role="img" aria-label="Photo of packaged A/C cage panels"></div></div><h2>A/C Cages</h2></div>
    <div class="product"><div class="thumb"><div class="t-accessory" role="img" aria-label="Image of a wire frame accessory"></div></div><h2>Accessories</h2></div>
  </section>
</main>
<footer>
  <div class="contactbar"><div class="wrap">
    <div class="item"><svg viewBox="0 0 12 12"><path d="M6 0a4 4 0 0 0-4 4c0 3 4 8 4 8s4-5 4-8a4 4 0 0 0-4-4zm0 2.5a1.5 1.5 0 1 1 0 3 1.5 1.5 0 0 1 0-3z" fill-rule="evenodd"/></svg>Level 6 250 Lorem Ipsm, Lorem Ipsm 3000</div>
    <div class="item"><svg viewBox="0 0 12 12"><rect width="12" height="12" rx="2"/><path d="M3 2.5h1.5l.7 2-1 .8a5 5 0 0 0 2.5 2.5l.8-1 2 .7V9c0 .4-.3.5-.6.5A6.5 6.5 0 0 1 2.5 3c0-.3.2-.5.5-.5z" fill="#0e0c0b"/></svg>123 456 789 000</div>
    <div class="item"><svg viewBox="0 0 12 12"><path d="M1 4h10v8H1zM3 0h6v4H3z"/></svg>123 456 789 000</div>
    <div class="item"><svg viewBox="0 0 12 12"><path d="M0 2h12v8H0z"/><path d="M0 2l6 4 6-4" stroke="#0e0c0b" fill="none"/></svg>info@domainname.com</div>
    <div class="social">
      <i class="s1"></i><i class="s2"></i><i class="s3"></i><i class="s4"></i>
    </div>
  </div></div>
  <div class="copyright">@ 2016 Ventora,Inc All Right Reserved.</div>
</footer>
</body>
</html>
```